Business card design needed

Family General Practitioner/ Family Physician.
Logo is the logo of the Crestmoor Guild of Family Clinicians Australia
http://kvplm.tarevo.edu.au/PictureGallery/logos/pages/CGFC%20logo_jpg.htm

Reason: Just a bit more time to make changes and the weekend for me to look at things closely and to choose. Thanks, Lumi

Thanks for all the submissions. So many of them are really works of art. Not one of them are not good. The ones that I am eliminating are the ones that I think are not suitable for me personally only, and because if I don't, it makes it very difficult to decide as many of you are also sending me slight variations of a card. I have just decided to choose a second place card too. Can't thank you all enough. Good luck, Lumi. P.S - Working today till 10 pm as the card says :-), so probably won't be able to give a feedback till late Saturday night or Sunday morning here in Sydney, Australia. 

Reason: Just added a second place to the budget and realised that Australia is ahead of the rest of the world in the time zone (only :-) - don't want to offend anyone or start a debate!! ) , so Monday deadline will mean it will be a weekend for the rest of the world. Just wanted to give everyone more time to submit their best, especially since I will be picking a second card too. Can't thank everyone enough for the submissions. P.S - Not keen on photos on the card.

Contact Information for Business Card

Dr. Lumi Harcourt M.B.B.S., F.C.G.F.C
Family General Practitioner
Address, timings, phone and fax number on the back.

Requirements
Must have
• Timings
Mon 7 am - 7 pm
Tues 7 am - 12 pm
Wed 7 am - 10 pm
Thurs 7 am - 12 pm
Fri 7 am - 8 pm
Sat 8 am - 10 pm
Sun - Off

```html
<!DOCTYPE html>
<html lang="en">
<head>
<meta charset="utf-8">
<title>Dr. Lumi Harcourt – Business Card</title>
<link rel="stylesheet" href="https://fonts.googleapis.com/css2?family=Cinzel:wght@500;700&family=Dancing+Script:wght@500&family=Open+Sans:wght@400;600&display=swap">
<style>
  :root {
    --backdrop: #e9e7e3;
    --paper: #ffffff;
    --navy: #1c4563;
    --band-top: #2e6485;
    --band-bottom: #123a55;
    --ink: #2a2a2a;
    --red: #c0272d;
  }
  * { box-sizing: border-box; margin: 0; padding: 0; }
  html, body { width: 1050px; height: 1200px; overflow: hidden; }
  body {
    background: var(--backdrop);
    display: flex; flex-direction: column; align-items: center; justify-content: center;
    gap: 60px;
  }
  .card {
    width: 840px; height: 480px;
    background: var(--paper);
    position: relative; overflow: hidden;
    box-shadow: 0 6px 18px rgba(0,0,0,.18);
  }

  /* Front */
  .tagline {
    position: absolute; left: 70px; top: 95px;
    font-family: "Dancing Script", cursive;
    font-size: 34px; color: var(--navy);
  }
  .guild-mark {
    position: absolute; right: 70px; top: 85px;
    display: flex; align-items: center; gap: 12px;
  }
  .guild-mark .square { width: 34px; height: 34px; background: var(--navy); }
  .guild-mark .name {
    font-family: "Cinzel", serif; font-weight: 700;
    font-size: 28px; color: var(--navy); letter-spacing: 2px;
  }
  .doctor-name {
    position: absolute; left: 100px; top: 232px;
    font-family: "Cinzel", serif; font-weight: 500;
    font-size: 38px; color: var(--navy); letter-spacing: 1px;
  }
  .band {
    position: absolute; left: 0; right: 0; bottom: 0; height: 196px;
    background: radial-gradient(ellipse at 30% 20%, var(--band-top), var(--band-bottom) 80%);
  }
  .credentials {
    position: absolute; left: 104px; top: 300px;
    font-family: "Cinzel", serif; color: #fff; line-height: 1.35;
  }
  .credentials .degrees { font-size: 20px; font-weight: 700; letter-spacing: 1px; }
  .credentials .role { font-size: 19px; font-weight: 500; }

  /* Back */
  .contact {
    position: absolute; left: 300px; top: 55px;
    font-family: "Open Sans", sans-serif; font-size: 26px; color: var(--ink); line-height: 1.3;
  }
  .timings-label {
    position: absolute; left: 90px; top: 130px; width: 190px; height: 60px;
    background: var(--navy); color: #fff;
    font-family: "Open Sans", sans-serif; font-weight: 600; font-size: 24px;
    display: flex; align-items: center; justify-content: center;
  }
  .hours {
    position: absolute; left: 110px; top: 205px;
    font-family: "Open Sans", sans-serif; color: var(--ink);
  }
  .schedule {
    font-size: 22px; line-height: 28px;
    border-collapse: collapse;
  }
  .schedule td { padding: 1px 0; }
  .schedule .day { width: 110px; }
  .closed {
    margin: 8px 0 0 190px;
    font-weight: 600; font-size: 28px; line-height: 34px; color: var(--red);
  }
</style>
</head>
<body>
  <section class="card card-front">
    <p class="tagline">"Caring about your health"</p>
    <div class="guild-mark">
      <span class="square"></span>
      <span class="name">CGFC</span>
    </div>
    <h1 class="doctor-name">Dr. Lumi Harcourt</h1>
    <div class="band"></div>
    <div class="credentials">
      <p class="degrees">M.B.B.S., F.C.G.F.C</p>
      <p class="role">Family General Practitioner</p>
    </div>
  </section>

  <section class="card card-back">
    <div class="contact">
      <p>phone: 00 000000</p>
      <p>fax: 00 000000</p>
    </div>
    <div class="timings-label">Timings:</div>
    <div class="hours">
      <table class="schedule">
        <tr><td class="day">Mon</td><td>7 am - 7 pm</td></tr>
        <tr><td class="day">Tues</td><td>7 am - 12 pm</td></tr>
        <tr><td class="day">Wed</td><td>7 am - 10 pm</td></tr>
        <tr><td class="day">Thurs</td><td>7 am - 12 pm</td></tr>
        <tr><td class="day">Fri</td><td>7 am - 8 pm</td></tr>
        <tr><td class="day">Sat</td><td>8 am - 10 pm</td></tr>
      </table>
      <p class="closed">Sun - Off</p>
    </div>
  </section>
</body>
</html>
```